Business Card Design Project

Hi I am after a business card double sided 1 side to have the attached PDF on front on the back:

Tavi Rundell - Managing Director
Mobile: 0412 638 274
email: tavi@pruvo.com.au
web: www.pruvo.com.au

Industry/Entity Type

Business

Font styles to use
Sans Serif

Requirements
Must have
• I want a classy looking card
Nice to have
• I like lime green and black and white

```html
<!DOCTYPE html>
<html lang="en">
<head>
<meta charset="utf-8">
<title>Pruvo Lawns and Gardens – Business Card</title>
<link href="https://fonts.googleapis.com/css2?family=Figtree:wght@300;400&display=swap" rel="stylesheet">
<style>
  :root {
    --lawn-green: #1db14b;
    --paper: #ffffff;
    --ink: #231f20;
    --backdrop: #ffffff;
  }
  * { margin: 0; padding: 0; box-sizing: border-box; }
  html, body {
    width: 1200px;
    height: 1000px;
    overflow: hidden;
    background: var(--backdrop);
    font-family: "Figtree", sans-serif;
  }
  .canvas { position: relative; width: 1200px; height: 1000px; }

  .card {
    position: absolute;
    left: 308px;
    width: 619px;
    height: 357px;
  }
  .card--front { top: 106px; background: var(--lawn-green); }
  .card--back  { top: 513px; background: var(--paper); outline: 1px solid #e6e6e6; }

  /* Front */
  .front-brand {
    position: absolute;
    left: 0; right: 0; top: 150px;
    display: flex;
    align-items: center;
    justify-content: center;
    gap: 14px;
  }
  .brand-mark {
    width: 44px; height: 44px;
    border-radius: 7px;
    background: var(--paper);
  }
  .brand-name {
    color: var(--paper);
    font-weight: 300;
    font-size: 26px;
    letter-spacing: 0.3px;
  }

  /* Back */
  .back-brand {
    position: absolute;
    left: 40px; top: 44px;
    display: flex;
    align-items: center;
    gap: 14px;
  }
  .back-brand .brand-mark {
    width: 63px; height: 63px;
    border-radius: 8px;
    background: var(--lawn-green);
  }
  .back-brand .brand-name { color: var(--lawn-green); font-size: 18px; }

  .contact {
    position: absolute;
    right: 50px;
    top: 116px;
    text-align: right;
    color: var(--ink);
    font-weight: 300;
  }
  .contact__name { font-size: 30px; line-height: 38px; }
  .contact__role { font-size: 21px; line-height: 28px; }
  .contact__lines { margin-top: 18px; }
  .contact__line {
    display: flex;
    justify-content: flex-end;
    align-items: center;
    gap: 14px;
    font-size: 23px;
    height: 36px;
    margin-bottom: 2px;
  }
  .contact__icon {
    width: 35px; height: 35px;
    border-radius: 5px;
    background: var(--lawn-green);
    display: flex; align-items: center; justify-content: center;
  }
  .contact__web {
    margin-top: 26px;
    margin-right: 2px;
    font-size: 21px;
  }
</style>
</head>
<body>
<main class="canvas">

  <section class="card card--front" aria-label="Card front">
    <div class="front-brand">
      <span class="brand-mark"></span>
      <span class="brand-name">Pruvo Lawns and Gardens</span>
    </div>
  </section>

  <section class="card card--back" aria-label="Card back">
    <div class="back-brand">
      <span class="brand-mark"></span>
      <span class="brand-name">Pruvo Lawns and Gardens</span>
    </div>

    <div class="contact">
      <p class="contact__name">Tavi Rundell</p>
      <p class="contact__role">Managing Director</p>
      <div class="contact__lines">
        <div class="contact__line">
          <span>0412 638 274</span>
          <span class="contact__icon">
            <svg width="16" height="24" viewBox="0 0 16 24" aria-hidden="true">
              <rect x="1" y="1" width="14" height="22" rx="2.5" fill="none" stroke="#fff" stroke-width="2"/>
              <rect x="3.5" y="4" width="9" height="13" fill="#fff"/>
              <circle cx="8" cy="20" r="1.3" fill="#fff"/>
            </svg>
          </span>
        </div>
        <div class="contact__line">
          <span>tavi@pruvo.com.au</span>
          <span class="contact__icon">
            <svg width="26" height="18" viewBox="0 0 26 18" aria-hidden="true">
              <rect x="1" y="1" width="24" height="16" fill="none" stroke="#fff" stroke-width="1.6"/>
              <path d="M1 1 L13 10 L25 1 M1 17 L10 8 M25 17 L16 8" fill="none" stroke="#fff" stroke-width="1.4"/>
            </svg>
          </span>
        </div>
      </div>
      <p class="contact__web">www.pruvo.com.au</p>
    </div>
  </section>

</main>
</body>
</html>
```